Restaurant menu design

Design fine dinning menu for Indian restaurant. Restaurant location is on river side. So if design has some touch of Yarra river of Melbourne and Indian touch. It is not compulsory. Creative and modern design is required.
I want to print in A3 and folded take away sizes so design should for both.
1. In A3, backside we need to design drink menu. I am attaching our current restaurant menu for drinks name and price.

Target Market(s)

Indian / Australian Customer

Industry/Entity Type

Indian Food, Indian fine dining

Colors
F0912C
F2A743
F7CA91
FBE8D2
FDF5EE

Requirements
Must have
• Simple but district design
Should not have
• common other restaurant type menu. Too many colours.

```html
<!DOCTYPE html>
<html lang="en">
<head>
<meta charset="utf-8">
<title>Mira's Kitchen — Food Menu</title>
<link href="https://fonts.googleapis.com/css2?family=Barlow:wght@300;400;500&display=swap" rel="stylesheet">
<style>
  :root {
    --saffron: #F0912C;
    --marigold: #F2A743;
    --apricot: #F7CA91;
    --sand: #FBE8D2;
    --paper: #FDF5EE;
    --ink: #1a1410;
    --ink-soft: #3a322b;
  }
  * { margin: 0; padding: 0; box-sizing: border-box; }
  html, body { width: 1200px; height: 848px; overflow: hidden; background: var(--paper); }
  .menu {
    position: relative;
    width: 1200px;
    height: 848px;
    overflow: hidden;
    background: var(--paper);
    font-family: "Barlow", Arial, sans-serif;
    color: var(--ink);
  }
  .river-line {
    position: absolute;
    left: 0;
    bottom: 0;
    width: 1200px;
    height: 24px;
  }
  .fold {
    position: absolute;
    top: 34px;
    width: 1px;
    height: 780px;
    background: var(--apricot);
  }
  .section-title {
    position: absolute;
    font-weight: 400;
    font-size: 20px;
    line-height: 28px;
    letter-spacing: 0.2px;
    white-space: nowrap;
    color: var(--saffron);
  }
  .list {
    position: absolute;
    font-size: 10.7px;
    line-height: 14.4px;
    white-space: nowrap;
  }
  .spaced .item { margin-bottom: 14.4px; }
  .item-name, .item-desc { display: block; }
  .item-name { font-weight: 500; }
  .item-desc { font-weight: 400; color: var(--ink-soft); }
  .item--light .item-name { text-transform: uppercase; font-weight: 500; }
  .item--light .item-desc { font-weight: 300; }
  .item--priced { position: relative; }
  .item-price {
    position: absolute;
    left: 282px;
    top: 0;
    font-weight: 500;
    color: var(--saffron);
  }
  .light-text .item-desc { font-weight: 300; }
</style>
</head>
<body>
<main class="menu">

  <span class="fold" style="left:384px;"></span>
  <span class="fold" style="left:818px;"></span>

  <svg class="river-line" viewBox="0 0 1200 24" aria-hidden="true">
    <path d="M0 14 C150 4 300 24 450 14 S750 4 900 14 S1100 22 1200 12" fill="none" stroke="var(--apricot)" stroke-width="1.2"/>
    <path d="M0 20 C150 10 300 30 450 20 S750 10 900 20 S1100 28 1200 18" fill="none" stroke="var(--sand)" stroke-width="1.2"/>
  </svg>

  <!-- Column one -->
  <h2 class="section-title" style="left:42px; top:33px;">VEGETARIAN ENTRÉES</h2>
  <div class="list spaced" style="left:42px; top:70px;">
    <div class="item item--light item--priced">
      <span class="item-name">Classic Samosa</span><span class="item-price">16</span>
      <span class="item-desc">Handcrafted pastry parcels filled with spiced<br>potatoes &amp; peas, served with a duo of fresh mint-<br>coriander chutney and sweet mango relish.</span>
    </div>
    <div class="item item--light item--priced">
      <span class="item-name">Crispy Onion &amp; Spinach Bhaji</span><span class="item-price">16</span>
      <span class="item-desc">Crisp golden fritters of baby spinach &amp; onion,<br>delicately spiced, paired with house chutneys.</span>
    </div>
    <div class="item item--priced">
      <span class="item-name" style="text-transform:uppercase;">Harabhara Edamame Kebab</span><span class="item-price">18</span>
      <span class="item-desc">Pan-seared medallions of edamame and garden<br>vegetables, stuffed with soft cheese and herbs,<br>served with tangy yogurt dip.</span>
    </div>
    <div class="item">
      <span class="item-name">Zafrani Paneer Tikka — $22</span>
      <span class="item-desc">Cubes of cottage cheese marinated in saffron,<br>cardamom &amp; smoky tandoor spices, grilled to<br>perfection, served with mint chutney and<br>microgreens.</span>
    </div>
    <div class="item">
      <span class="item-name">Vada Pav Sliders — $16</span>
      <span class="item-desc">A gourmet take on Mumbai’s street legend: spiced<br>potato croquette in a butter brioche bun, layered<br>with tamarind, mint-coriander chutney &amp; fiery<br>thecha, accompanied by crisp fried green chilli.</span>
    </div>
  </div>

  <h2 class="section-title" style="left:42px; top:446px;">NON VEGETARIAN ENTRÉES</h2>
  <div class="list" style="left:42px; top:484px;">
    <div class="item"><span class="item-name">Smoke Tandoori Chicken Tikka — $20</span><span class="item-desc">Charcoal-grilled chicken marinated overnight<br>with aromatic spices, finished with a touch of<br>smokey infusion.</span></div>
    <div class="item"><span class="item-name">Chicken Malai Tikka — $20</span><span class="item-desc">Tender chicken morsels marinated in cream,<br>cheese &amp; cardamom, cooked gently in the<br>tandoor for a melt-in-mouth experience.</span></div>
    <div class="item"><span class="item-name">Awadhi Fish Tikka — $22</span><span class="item-desc">Fresh barramundi fillets marinated with hand-<br>pounded Awadhi spices, grilled for a delicate<br>smokey finish.</span></div>
    <div class="item"><span class="item-name">Tandoori Tiger Prawns — $24</span><span class="item-desc">Jumbo prawns infused with curry-leaf butter,<br>garlic &amp; chilli, char-grilled for an indulgent<br>coastal flavour.</span></div>
    <div class="item"><span class="item-name">Lamb Gilafi Seekh — $22</span><span class="item-desc">Minced lamb spiced with herbs, peppers &amp;<br>aromatics, skewered &amp; flame-roasted, served<br>with minted yogurt.</span></div>
    <div class="item"><span class="item-name">Tandoori Platter — $39</span><span class="item-desc">A fine selection of assorted tandoori classics,<br>served with mint chutney.</span></div>
  </div>

  <!-- Column two -->
  <h2 class="section-title" style="left:404px; top:33px;">CHAAT</h2>
  <div class="list" style="left:404px; top:69px;">
    <div class="item"><span class="item-name">Panipuri Experience — $20</span><span class="item-desc">Crisp puris filled with spiced potato, tangy<br>chutneys &amp; chilled spiced water — a refined<br>version of the street favourite.</span></div>
    <div class="item"><span class="item-name">Burrata Chaat — $20</span><span class="item-desc">Creamy burrata resting on crispy papdi, layered<br>with tamarind glaze, mint chutney &amp; golden<br>sev.</span></div>
    <div class="item"><span class="item-name">Deconstructed Samosa Chaat — $18</span><span class="item-desc">Crispy samosa pastry crumbles over spiced<br>potato &amp; peas, dressed with chutneys, yogurt &amp;<br>pomegranate jewels.</span></div>
  </div>

  <h2 class="section-title" style="left:405px; top:275px;">INDO-CHINESE</h2>
  <div class="list" style="left:404px; top:318px;">
    <div class="item"><span class="item-name">Vegetable Manchurian Dry — $22</span><span class="item-desc">Golden-fried vegetable dumplings wok-tossed<br>in garlic, chilli &amp; soy glaze.</span></div>
    <div class="item"><span class="item-name">Paneer Chilli Dry — $24</span><span class="item-desc">Cottage cheese cubes tossed with peppers,<br>onions &amp; chilli-garlic soy reduction.</span></div>
    <div class="item"><span class="item-name">Chilli Chicken Dry — $26</span><span class="item-desc">Tender chicken tossed with shallots, peppers &amp;<br>fiery Indo-Chinese sauce.</span></div>
    <div class="item"><span class="item-name">Oriental Noodles — Veg $22 / Chicken $24</span><span class="item-desc">Stir-fried noodles with seasonal vegetables,<br>wok-seared with soy &amp; garlic.</span></div>
  </div>

  <h2 class="section-title" style="left:405px; top:521px;">CLASSIC CURRIES</h2>
  <div class="list" style="left:405px; top:555px;">
    <div class="item"><span class="item-name">Paneer / Kofta / Mixed Veg — $26</span><span class="item-desc">Choose your protein with a choice of gourmet curry bases.</span></div>
    <div class="item"><span class="item-name">Chicken / Lamb — $28</span><span class="item-desc">Choose your protein with a choice of gourmet curry bases.</span></div>
    <div class="item"><span class="item-name">Prawns / Fish — $30</span><span class="item-desc">Choose your protein with a choice of gourmet curry bases.</span></div>
    <div class="item"><span class="item-name">Vindaloo —</span><span class="item-desc">Fiery Goan-style curry with red chillies &amp; vinegar.</span></div>
    <div class="item"><span class="item-name">Saag —</span><span class="item-desc">Creamy buttered spinach slow-cooked with spices.</span></div>
    <div class="item"><span class="item-name">Korma —</span><span class="item-desc">Mild, creamy cashew &amp; saffron curry.</span></div>
    <div class="item"><span class="item-name">Masala —</span><span class="item-desc">Tomato &amp; onion base enriched with cream &amp; butter.</span></div>
    <div class="item"><span class="item-name">Madras —</span><span class="item-desc">Coconut-based curry with onions, garlic &amp; curry leaves.</span></div>
  </div>

  <!-- Column three -->
  <h2 class="section-title" style="left:842px; top:33px;">MIRA’S KITCHEN SPECIAL<br>VEGETARIAN CURRIES</h2>
  <div class="list light-text" style="left:842px; top:104px;">
    <div class="item"><span class="item-name">Sham Savera Kofta — $26</span><span class="item-desc">Spinach dumplings filled with cottage cheese, simmered in<br>a rich tomato-butter sauce — a true royal delicacy.</span></div>
    <div class="item"><span class="item-name">Mexican Salsa Paneer — $28</span><span class="item-desc">Paneer cubes tossed in a fusion of roasted Mexican-style<br>tomato salsa and Indian spices — a bold East-meets-West<br>creation.</span></div>
    <div class="item"><span class="item-name">Mushroom Mutter Masala — $28</span><span class="item-desc">Tender mushrooms and garden peas in a spiced onion-<br>tomato gravy, finished with cream.</span></div>
    <div class="item"><span class="item-name">Kaju Curry — $28</span><span class="item-desc">A luxurious cashew-based curry enriched with aromatic<br>spices, velvety texture &amp; buttery finish.</span></div>
    <div class="item"><span class="item-name">Cheese Butter Masala — $28</span><span class="item-desc">Paneer and soft cheese in a creamy, butter-rich tomato<br>gravy — indulgent &amp; comforting.</span></div>
    <div class="item"><span class="item-name">Dal Tadka — $22</span><span class="item-desc">Yellow lentils tempered with garlic, cumin &amp; chilli, offering<br>homestyle comfort with gourmet finesse.</span></div>
    <div class="item"><span class="item-name">Dal Makhani — $22</span><span class="item-desc">Black lentils, slow-cooked overnight with butter and cream<br>— a timeless Delhi specialty.</span></div>
    <div class="item"><span class="item-name">Vegetable Dum Biryani — $28</span><span class="item-desc">Saffron-scented basmati rice layered with seasonal<br>vegetables, sealed and slow-cooked in the dum style,<br>served with cooling raita.</span></div>
  </div>

  <h2 class="section-title" style="left:842px; top:488px;">RICE &amp; BIRYANIS</h2>
  <div class="list light-text" style="left:842px; top:520px;">
    <div class="item"><span class="item-name">Plain Basmati Rice — $8</span><span class="item-desc">Steamed long-grain basmati rice, light &amp; fluffy.</span></div>
    <div class="item"><span class="item-name">Jeera Rice — $8</span><span class="item-desc">Basmati rice tempered with roasted cumin seeds.</span></div>
    <div class="item"><span class="item-name">Lemon Coconut Rice — $10</span><span class="item-desc">Fragrant rice infused with lemon zest, curry leaves &amp;<br>coconut.</span></div>
    <div class="item"><span class="item-name">Peas Pulao — $10</span><span class="item-desc">Delicate basmati rice cooked with sweet garden peas &amp;<br>whole spices.</span></div>
    <div class="item"><span class="item-name">Biryani Flavoured Rice — $15</span><span class="item-desc">Aromatic saffron basmati rice prepared in biryani style.</span></div>
    <div class="item"><span class="item-name">Vegetable Dum Biryani — $28</span><span class="item-desc">Classic layered vegetable biryani with saffron, slow-cooked<br>dum style.</span></div>
    <div class="item"><span class="item-name">Hyderabadi Chicken Biryani — $30</span><span class="item-desc">Fragrant rice layered with marinated chicken, spices &amp;<br>saffron, served with raita.</span></div>
    <div class="item"><span class="item-name">Lamb Dum Biryani — $33</span><span class="item-desc">A celebratory lamb shank biryani, slow-cooked with<br>saffron, mint &amp; caramelised onions.</span></div>
  </div>

</main>
</body>
</html>
```